Investment Group needs a web page design

We need a web page design for a San Francisco-based investment group called 'Valtrimor LLC'. The final design should be stylish and attractive to the idea while retaining a sense of stability and professionalism. A great example is http://brindlewoodholdings.com/.

I am attaching the group's logo which should be the base for the webpage design.
Updates

Please note that I am interested in a single webpage that presents basic information. See the following example: http://brindlewoodholdings.com/

Target Market(s)

persons doing initial due diligence and trying to assess what kind of group we are.

Industry/Entity Type

Investment

Font styles to use
Serif

Colors
86acd3
3176b5
0355a3

Requirements
Nice to have
• Would love the design to incorporate the concept - 'Sen no Sen: a block and counter attack while the opponent is attacking.'
Should not have
• Do not include trite illustrations related to finance, money or investing.

```html
<!DOCTYPE html>
<html lang="en">
<head>
<meta charset="utf-8">
<title>Valtrimor LLC</title>
<link href="https://fonts.googleapis.com/css2?family=Jost:wght@400;500;600&display=swap" rel="stylesheet">
<style>
  :root {
    --white: #ffffff;
    --ink: #111111;
    --brand-pale: #86acd3;
    --brand-mid: #3176b5;
    --brand-deep: #0355a3;
    --band-navy: #0d3f82;
  }
  * { box-sizing: border-box; margin: 0; padding: 0; }
  html, body { width: 1200px; height: 990px; overflow: hidden; }
  body { font-family: "Jost", Arial, sans-serif; background: var(--white); color: var(--ink); position: relative; }

  .site-header { position: absolute; top: 0; left: 0; width: 1200px; height: 88px; background: var(--white); }
  .brand { position: absolute; left: 160px; top: 34px; display: flex; align-items: center; gap: 6px; }
  .brand-mark { width: 28px; height: 28px; background: var(--ink); }
  .brand-name { font-size: 31px; font-weight: 400; letter-spacing: 0.5px; line-height: 1; color: var(--ink); }
  .main-nav { position: absolute; top: 45px; left: 435px; display: flex; gap: 0; font-size: 13px; font-weight: 500; }
  .main-nav a { position: absolute; white-space: nowrap; color: var(--ink); text-decoration: none; }
  .main-nav a.is-active { color: var(--brand-mid); }
  .login-button { position: absolute; left: 965px; top: 41px; width: 74px; height: 25px; background: var(--brand-deep); color: var(--white); font-size: 13px; font-weight: 500; display: flex; align-items: center; justify-content: center; }

  .hero { position: absolute; top: 88px; left: 0; width: 1200px; height: 559px;
    background: linear-gradient(180deg, #f6c45c 0%, #f1a43e 22%, #b9874e 42%, #6d6552 62%, #4a4d4a 82%, #3c403f 100%); }
  .hero-caption { position: absolute; top: 487px; width: 100%; text-align: center; color: var(--white); font-size: 21px; font-weight: 400; }
  .hero-dots { position: absolute; top: 528px; left: 565px; display: flex; gap: 6px; }
  .hero-dots span { width: 13px; height: 13px; border-radius: 50%; background: var(--white); }
  .hero-dots span.is-current { background: var(--brand-deep); }

  .welcome { position: absolute; top: 647px; left: 0; width: 1200px; height: 241px; background: var(--band-navy); color: var(--white); text-align: center; }
  .welcome-title { position: absolute; top: 38px; width: 100%; font-size: 17px; font-weight: 600; }
  .welcome-text { position: absolute; top: 73px; left: 200px; width: 800px; font-size: 14px; line-height: 22px; }
  .cta-button { position: absolute; left: 507px; top: 160px; width: 187px; height: 47px; background: var(--brand-pale); color: var(--white); font-size: 16px; font-weight: 600; display: flex; align-items: center; justify-content: center; }

  .site-footer { position: absolute; top: 888px; left: 0; width: 1200px; height: 102px; background: var(--brand-mid); color: var(--white); }
  .footer-nav { position: absolute; top: 24px; left: 161px; display: flex; font-size: 14px; }
  .footer-nav a { color: var(--white); text-decoration: none; }
  .footer-nav .sep { margin: 0 18px; }
  .copyright { position: absolute; top: 55px; left: 161px; font-size: 14px; }
  .social-links { position: absolute; top: 38px; left: 952px; display: flex; gap: 8px; }
  .social-links span { width: 24px; height: 24px; border-radius: 50%; background: var(--white); }
</style>
</head>
<body>
  <header class="site-header">
    <div class="brand"><span class="brand-mark"></span><span class="brand-name">VALTRIMOR</span></div>
    <nav class="main-nav">
      <a class="is-active" style="left:0">HOME</a>
      <a style="left:66px">ABOUT US</a>
      <a style="left:155px">INVESTMENTS</a>
      <a style="left:266px">SERVICES</a>
      <a style="left:351px">FAQ’S</a>
      <a style="left:415px">CONTACT US</a>
    </nav>
    <div class="login-button">LOGIN</div>
  </header>

  <section class="hero" role="img" aria-label="Aerial view of San Francisco downtown at sunset with the bay in the distance">
    <p class="hero-caption">Neque porro quisquam est qui dolorem ipsum quia dolor sit amet ...</p>
    <div class="hero-dots"><span class="is-current"></span><span></span><span></span><span></span></div>
  </section>

  <section class="welcome">
    <h1 class="welcome-title">WELCOME TO VALTRIMOR</h1>
    <p class="welcome-text">Lorem Ipsum is simply dummy text of the printing and typesetting industry. Lorem Ipsum has been the industry's standard dummy text ever since the 1500s, when an unknown printer took a galley of type and scrambled it to make a type specimen book. It has survived not only five centuries, but also the leap into electronic typesetting, remaining essentially unchanged.</p>
    <div class="cta-button">Get Started To Invest</div>
  </section>

  <footer class="site-footer">
    <nav class="footer-nav">
      <a>Home</a><span class="sep">|</span><a>About Us</a><span class="sep">|</span><a>Investments</a><span class="sep">|</span><a>Services</a><span class="sep">|</span><a>FAQ’s</a><span class="sep">|</span><a>Contact Us</a>
    </nav>
    <p class="copyright">© 2014 Company Name ,All Rights reserved</p>
    <div class="social-links"><span></span><span></span><span></span></div>
  </footer>
</body>
</html>
```